Interior Design business card design

I am an interior decorator - dont want to specify decorating more just design.
Want organic looking logo - charcoal and white - with touch of lime green.
Like the idea of some sort of spiral in corner but writing in a line
want lower case, tildamarchetti as one and designs in different font underneath. Maybe using t and m as logo.
More modern than traditional. My clients are mid to top end residential

Target Market(s)

medium to top end homeowners

Industry/Entity Type

Residential

Contact Information for Business Card

Tilda Marchetti Designs
58 Kellaway ave
Pemberly 2190 NSW
Tel 0417268914
tildamarchetti@velnaro.com.au

Logo Text

Tilda Marchetti Designs

Logo styles of interest
Abstract Logo
Lettermark Logo
Requirements
Must have
• Name address ph and e mail
Nice to have
• Contemporary
smart but organic
Should not have
• no traditional fonts

```html
<!DOCTYPE html>
<html lang="en">
<head>
<meta charset="utf-8">
<title>Tilda Marchetti Designs – Business Card</title>
<link rel="stylesheet" href="https://fonts.googleapis.com/css2?family=Questrial&display=swap">
<style>
  :root {
    --backdrop: #e4e4e6;
    --card-light: #f3f3f3;
    --card-dark: #55555f;
    --charcoal: #4d4d57;
    --soft-grey: #c9c9cc;
    --text-dark: #4a4a52;
    --text-light: #d6d6da;
    --lime: #7cc520;
  }
  * { margin: 0; padding: 0; box-sizing: border-box; }
  html, body {
    width: 1200px; height: 961px; overflow: hidden;
    background: var(--backdrop);
    font-family: "Questrial", "Century Gothic", sans-serif;
  }
  .stage {
    position: relative; width: 1200px; height: 961px;
  }
  .card {
    position: absolute; left: 330px;
    width: 540px; height: 300px;
    border-radius: 26px;
    overflow: hidden;
    box-shadow: 0 6px 18px rgba(0,0,0,0.12);
  }
  .card--front { top: 130px; background: var(--card-light); color: var(--text-dark); }
  .card--back { top: 530px; background: var(--card-dark); color: var(--text-light); }

  .wordmark {
    position: absolute;
    font-size: 27px; letter-spacing: 0.2px; white-space: nowrap;
  }
  .card--front .wordmark { top: 48px; left: 205px; color: var(--text-dark); }
  .card--back .wordmark { top: 150px; left: 40px; color: var(--text-light); }

  .mark-square { position: absolute; }
  .card--front .mark-square { top: 110px; left: 50px; width: 100px; height: 100px; background: var(--charcoal); }
  .card--back .mark-square { top: 30px; right: 40px; width: 140px; height: 140px; background: var(--soft-grey); }

  .contact {
    position: absolute; font-size: 13px; line-height: 20px; white-space: nowrap;
  }
  .card--front .contact { right: 36px; bottom: 40px; text-align: right; }
  .card--back .contact { left: 40px; bottom: 36px; text-align: left; }
  .contact-row { display: flex; align-items: center; gap: 14px; }
  .card--front .contact-row { justify-content: flex-end; }
  .contact-item { display: inline-flex; align-items: center; gap: 6px; }
  .icon { width: 13px; height: 13px; display: block; }
</style>
</head>
<body>
<main class="stage">
  <section class="card card--front" aria-label="Business card front">
    <div class="mark-square" aria-hidden="true"></div>
    <p class="wordmark">tildamarchetti designs</p>
    <div class="contact">
      <p class="address">58 Kellaway ave Pemberly 2190 NSW</p>
      <div class="contact-row">
        <span class="contact-item">
          <svg class="icon" viewBox="0 0 14 14" aria-hidden="true"><circle cx="7" cy="7" r="7" fill="var(--lime)"/><path d="M4.4 3.6l1.4-.2.7 1.7-.9.7c.4.9 1.1 1.6 2 2l.7-.9 1.7.7-.2 1.4c-3 .2-5.6-2.4-5.4-5.4z" fill="#fff"/></svg>
          0417268914
        </span>
        <span class="contact-item">
          <svg class="icon" viewBox="0 0 14 14" aria-hidden="true"><circle cx="7" cy="7" r="7" fill="var(--lime)"/><rect x="3.5" y="4.5" width="7" height="5" fill="#fff"/><path d="M3.5 4.5L7 7.3l3.5-2.8" fill="none" stroke="var(--lime)" stroke-width="0.8"/></svg>
          tildamarchetti@velnaro.com.au
        </span>
      </div>
    </div>
  </section>

  <section class="card card--back" aria-label="Business card back">
    <div class="mark-square" aria-hidden="true"></div>
    <p class="wordmark">tildamarchetti designs</p>
    <div class="contact">
      <p class="address">58 Kellaway ave Pemberly 2190 NSW</p>
      <div class="contact-row">
        <span class="contact-item">
          <svg class="icon" viewBox="0 0 14 14" aria-hidden="true"><circle cx="7" cy="7" r="7" fill="var(--lime)"/><path d="M4.4 3.6l1.4-.2.7 1.7-.9.7c.4.9 1.1 1.6 2 2l.7-.9 1.7.7-.2 1.4c-3 .2-5.6-2.4-5.4-5.4z" fill="#fff"/></svg>
          0417268914
        </span>
        <span class="contact-item">
          <svg class="icon" viewBox="0 0 14 14" aria-hidden="true"><circle cx="7" cy="7" r="7" fill="var(--lime)"/><rect x="3.5" y="4.5" width="7" height="5" fill="#fff"/><path d="M3.5 4.5L7 7.3l3.5-2.8" fill="none" stroke="var(--lime)" stroke-width="0.8"/></svg>
          tildamarchetti@velnaro.com.au
        </span>
      </div>
    </div>
  </section>
</main>
</body>
</html>
```